Vodka label for New Brand called KIRO Vodka

We need a label measuring 3.5 inches wide & 5 inches tall for this vodka bottle. The brand is "KIRO Vodka". This should be the largest font on the label. "Handcrafted in the USA" should be on bottle in small font near the bottom. The tagline "Keeping It Real Onward" also needs to be included anywhere that makes sense in a smaller font than the brand name. Also in smaller font at the bottom/corners- "80 proof, 750 ml, 40% alc/vol" I value the human mind over AI, but am providing a couple designs that were AI generated to give you a better idea where to start and what we are looking for. Thank you!

Target Market(s)

21-45 year olds.

Industry/Entity Type

Alcohol

Colors
0054AA
0677BA
7BADD7
CADEEF
E8F1F8
EB3D1F
EC4F4E
F09395
F8D3D4
FCEDEE

Requirements
Should not have
• You can not use the US flag but can use elements of it.

```html
<!DOCTYPE html>
<html lang="en">
<head>
<meta charset="utf-8">
<title>KIRO Vodka – Label</title>
<link rel="stylesheet" href="https://fonts.googleapis.com/css2?family=Bodoni+Moda:opsz,wght@6..96,700&family=Allura&family=Work+Sans:wght@400;500&display=swap">
<style>
  :root {
    --label-red: #eb3d1f;
    --backdrop: #fcedee;
    --ink: #2b2226;
    --rule: #3a2226;
  }
  html, body {
    margin: 0;
    padding: 0;
    width: 1200px;
    height: 900px;
    overflow: hidden;
    background: var(--backdrop);
  }
  .label {
    position: absolute;
    left: 285px;
    top: 0;
    width: 630px;
    height: 900px;
    background: var(--label-red);
    color: var(--ink);
  }
  .frame-rules {
    position: absolute;
    inset: 0;
  }
  .brand-name {
    position: absolute;
    left: 0;
    right: 0;
    top: 280px;
    margin: 0;
    text-align: center;
    font-family: "Bodoni Moda", "Didot", serif;
    font-weight: 700;
    font-size: 112px;
    line-height: 104px;
    letter-spacing: 4px;
    color: var(--ink);
  }
  .brand-name span { display: block; }
  .tagline {
    position: absolute;
    left: 0;
    right: 0;
    top: 516px;
    margin: 0;
    text-align: center;
    font-family: "Work Sans", "Helvetica", sans-serif;
    font-weight: 500;
    font-size: 16px;
    letter-spacing: 1.4px;
    text-transform: uppercase;
    color: var(--ink);
  }
  .origin {
    position: absolute;
    left: 0;
    right: 0;
    top: 722px;
    margin: 0;
    text-align: center;
    font-family: "Allura", cursive;
    font-size: 36px;
    color: var(--ink);
  }
  .spec {
    position: absolute;
    top: 800px;
    margin: 0;
    font-family: "Work Sans", "Helvetica", sans-serif;
    font-size: 13px;
    letter-spacing: 0.3px;
    text-transform: uppercase;
    color: var(--ink);
  }
  .spec--proof { left: 50px; }
  .spec--volume { right: 50px; }
</style>
</head>
<body>
<main class="label">
  <svg class="frame-rules" width="630" height="900" viewBox="0 0 630 900" aria-hidden="true">
    <g stroke="var(--rule)" stroke-width="1.5" fill="none">
      <line x1="48" y1="50" x2="210" y2="50"/>
      <line x1="420" y1="50" x2="582" y2="50"/>
      <line x1="48" y1="850" x2="210" y2="850"/>
      <line x1="420" y1="850" x2="582" y2="850"/>
      <line x1="30" y1="74" x2="30" y2="400"/>
      <line x1="30" y1="500" x2="30" y2="826"/>
      <line x1="600" y1="74" x2="600" y2="400"/>
      <line x1="600" y1="500" x2="600" y2="826"/>
    </g>
  </svg>

  <h1 class="brand-name"><span>KIRO</span><span>VODKA</span></h1>
  <p class="tagline">Keeping It Real Onward</p>
  <p class="origin">Handcrafted in the USA</p>
  <p class="spec spec--proof">80 Proof</p>
  <p class="spec spec--volume">750 ml,&nbsp; 40% Alc/Vol</p>
</main>
</body>
</html>
```